Brightford Lingua Partners, LLC

We need a business card that includes information about our business and conveys a reliable business that provides document translation services and interpreters for a variety of corporate and individual clients. We want to come across as professional, reliable, yet approachable. It should include the following on one side:

ESL / ENL Language Classes, Private Lessons, and Online Tutors
PALQE Training and Testing
Translating & Interpreting Services
Contact us about Over-the-Phone Interpreting in over 200 languages
24/7/365
www.brightfordlingua.example

The other side should include (555) 481-3062

Marla Quennick, President
412 Garvin Ave., Ste. 209
Indianapolis, IN 46999
Updates

Please add USA as part of the address. Also, please add mrqquennick@brightfordlinguapartners.example as the e-mail address. Thank you.

Target Market(s)

Business professionals, their families, the international community

Industry/Entity Type

Business

Contact Information for Business Card

24/7/365
www.brightfordlingua.example

(555) 481-3062

Marla Quennick, President
412 Garvin Ave., Ste. 209
Indianapolis, IN 46999
USA

Font styles to use
Sans Serif

Colors

Designer to choose colors to be used in the design.

Requirements
Must have
• See project description
• e-mail address and web address
• Phone number
Nice to have
• a globe
• physical address
Should not have
• Should not have the same color scheme as other agencies in our market in Indiana unless it is blue and black. No purple or yellow.

```html
<!DOCTYPE html>
<html lang="en">
<head>
<meta charset="utf-8">
<title>Brightford Lingua Partners – Business Card</title>
<link href="https://fonts.googleapis.com/css2?family=Source+Sans+3:wght@400;600&display=swap" rel="stylesheet">
<style>
  :root {
    --bg: #e9e8e9;
    --ink: #1a1a1a;
    --brand-blue: #1f8ad6;
    --blue-deep: #0d4f99;
    --blue-mid: #1570c4;
    --blue-light: #2a96d8;
    --paper: #ffffff;
    --on-blue: #ffffff;
  }
  * { box-sizing: border-box; margin: 0; padding: 0; }
  html, body { width: 1200px; height: 900px; overflow: hidden; }
  body {
    background: var(--bg);
    font-family: "Source Sans 3", sans-serif;
    color: var(--ink);
    position: relative;
  }
  .card {
    position: absolute;
    left: 285px;
    width: 630px;
    height: 360px;
    border-radius: 26px;
    overflow: hidden;
    box-shadow: 0 10px 24px rgba(0,0,0,0.18);
  }

  /* Front */
  .card-front { top: 470px; background: var(--paper); }
  .brand {
    position: absolute; left: 40px; top: 70px;
    display: flex; align-items: center; gap: 14px;
  }
  .brand-dot {
    width: 70px; height: 70px; border-radius: 50%;
    background: var(--brand-blue); flex: none;
  }
  .brand-name {
    font-weight: 600; font-size: 25px; line-height: 1.05;
    color: var(--ink); width: 150px;
  }
  .contact {
    position: absolute; left: 280px; top: 74px;
    list-style: none;
  }
  .rule {
    width: 70px; height: 3px; background: var(--brand-blue);
  }
  .contact-list { list-style: none; margin: 18px 0; }
  .contact-list li {
    display: flex; align-items: center; gap: 8px;
    font-size: 15.5px; line-height: 26px;
  }
  .contact-list svg { width: 15px; height: 15px; flex: none; fill: var(--brand-blue); }
  .address {
    position: absolute; left: 40px; bottom: 46px;
    display: flex; align-items: center; gap: 8px;
    font-size: 16px;
  }
  .address svg { width: 14px; height: 18px; fill: var(--brand-blue); }

  /* Back */
  .card-back {
    top: 60px;
    background: linear-gradient(120deg, var(--blue-deep) 0%, var(--blue-mid) 45%, var(--blue-light) 100%);
    color: var(--on-blue);
  }
  .globe-area {
    position: absolute; left: 120px; top: -60px;
    width: 360px; height: 360px; border-radius: 50%;
    background: radial-gradient(circle at 55% 45%, rgba(255,255,255,0.14), rgba(10,60,130,0.35) 70%);
  }
  .back-brand {
    position: absolute; left: 190px; top: 54px;
    display: flex; align-items: center; gap: 14px;
  }
  .back-brand .brand-dot {
    width: 84px; height: 84px; background: rgba(255,255,255,0.85);
  }
  .back-brand .brand-name { color: var(--ink); font-size: 30px; width: 190px; }
  .services {
    position: absolute; left: 0; right: 0; top: 200px;
    text-align: center; font-size: 16px; line-height: 27px;
  }
  .services .sep { margin: 0 10px; }
</style>
</head>
<body>

  <section class="card card-back" aria-label="Card back">
    <div class="globe-area" role="img" aria-label="Globe illustration"></div>
    <div class="back-brand">
      <span class="brand-dot"></span>
      <span class="brand-name">Brightford Lingua Partners, LLC</span>
    </div>
    <div class="services">
      <p>ESL / ENL Language Classes, Private Lessons and Online Tutors</p>
      <p>PALQE Training and Testing<span class="sep">/</span>Translating &amp; Interpreting Services</p>
      <p>Contact us about Over-the-Phone Interpreting in over 200 languages 24/7/365</p>
    </div>
  </section>

  <section class="card card-front" aria-label="Card front">
    <div class="brand">
      <span class="brand-dot"></span>
      <span class="brand-name">Brightford Lingua Partners, LLC</span>
    </div>
    <div class="contact">
      <div class="rule"></div>
      <ul class="contact-list">
        <li>
          <svg viewBox="0 0 16 16" aria-hidden="true"><path d="M2 6c0-2 2-3 6-3s6 1 6 3l-2 1-1-2H5L4 7 2 6zm2 2h8l1 5H3l1-5zm4 1.2a1.6 1.6 0 1 0 0 3.2 1.6 1.6 0 0 0 0-3.2z"/></svg>
          (555) 481-3062
        </li>
        <li>
          <svg viewBox="0 0 16 16" aria-hidden="true"><path d="M1 3h14v10H1V3zm1.5 1.2L8 8.5l5.5-4.3H2.5zM2 5.3V12h12V5.3L8 10 2 5.3z"/></svg>
          mrqquennick@brightfordlinguapartners.example
        </li>
        <li>
          <svg viewBox="0 0 16 16" aria-hidden="true"><path d="M8 1a7 7 0 1 0 0 14A7 7 0 0 0 8 1zm0 1.3c.8 0 1.7 1.5 2 3.7H6c.3-2.2 1.2-3.7 2-3.7zM2.4 7h2.5v2H2.4a5.7 5.7 0 0 1 0-2zm3.5 0h4.2v2H5.9V7zm5.2 0h2.5a5.7 5.7 0 0 1 0 2h-2.5V7zM6 10h4c-.3 2.2-1.2 3.7-2 3.7S6.3 12.2 6 10z"/></svg>
          www.brightfordlingua.example
        </li>
      </ul>
      <div class="rule"></div>
    </div>
    <p class="address">
      <svg viewBox="0 0 14 18" aria-hidden="true"><path d="M7 0a6 6 0 0 0-6 6c0 4.5 6 12 6 12s6-7.5 6-12a6 6 0 0 0-6-6zm0 8.4A2.4 2.4 0 1 1 7 3.6a2.4 2.4 0 0 1 0 4.8z"/></svg>
      Marla Quennick, President, 412 Garvin Ave., Ste. 209, Indianapolis, IN 46999, USA
    </p>
  </section>

</body>
</html>
```